Trucking Insurance Website Design

We are working with a Trucking Insurance company in California. They provide vehicle insurance for trucking companies and truckers.
As you might imagine, there are no websites we could find for inspiration for trucking insurance. But below are sites that do similar insurance.
https://pinemeadowcover.com/trucking-insurance/
https://www.haulsafeplan.com/california-commercial-truck-insurance
Thank you for taking the time to consider designing a website for us. We are web developers based in Stockton, CA, USA. Most of our projects go through the same process. Understanding this process may help you win a project with us. We custom-code all of our websites in-house. We don’t have any requirements as to what tools you use for your design, but we ask that you follow these guidelines.
IMAGES:
If you use any images or icons in the design, we ask that you have a link to the asset so we can purchase the image/icon. Most of the designs we submit do not have the customer’s images on them unless they have some great images. Be creative; show us the feeling you are trying to portray with your image choices. Use any royalty-free site you choose. We subscribe to Quillon and mainly use their images, but we can purchase images outside of Quillon. PLEASE NOTE: we will not submit designs to clients with watermarks on the images.
FONTS:
We ask that you identify the fonts you’re using in the design. This can be done in a message if you want. We typically use Tavlo Fonts and Quillon Fonts.
CONTENT:
We're always open to different content and ideas. We often submit designs with stock images so the client can see our vision. We typically take pictures after the website launch to use their images with our vision. Lorem Ipsum is fine for paragraphs, but we ask that you make the Headers with correct English. We want to be able to show the vision and identify the sections of the website.
INSPIRATION:
We typically add a couple of links in the brief of websites we like to help you get started in your design.
REVISIONS:
We do not often ask for revisions of the designs unless we see something in the design that may not appeal to the client. If there are slight changes that we want to make, we do that in the development process.
FEEDBACK:
We rarely give feedback on designs during the design process. We are working on many website projects and do not have the time to provide feedback. We usually respond if your request is well thought out and asks specific questions, but a note asking “feedback, please” usually goes unanswered.
1 page

```html
<!DOCTYPE html>
<html lang="en">
<head>
<meta charset="utf-8">
<title>Ridgeline Insurance – Trucking Insurance</title>
<link rel="stylesheet" href="https://fonts.googleapis.com/css2?family=Montserrat:wght@400;500;600;700;800&display=swap">
<style>
:root{
  --red:#c8102e;
  --red-dark:#a50d25;
  --blue:#4a4fb5;
  --blue-title:#3b48a6;
  --ink:#1b1b1b;
  --text:#555;
  --muted:#8a8a8a;
  --line:#e4e4e4;
  --footer:#e6e6e6;
  --white:#fff;
}
*{box-sizing:border-box;margin:0;padding:0}
html,body{width:1200px;height:4880px;overflow:hidden}
body{font-family:'Montserrat',sans-serif;color:var(--ink);background:var(--white);position:relative}
.abs{position:absolute}
a{color:inherit;text-decoration:none}
.btn{display:inline-flex;align-items:center;justify-content:center;font-weight:600;font-size:15px;border-radius:6px}
.btn-blue{background:var(--blue);color:var(--white);width:140px;height:50px}
.btn-ghost{border:1.5px solid var(--white);color:var(--white);background:transparent;width:150px;height:44px;border-radius:4px}
.section-title{font-size:38px;font-weight:700;color:var(--ink)}
.section-title .accent{color:var(--red)}
.centered{left:0;width:1200px;text-align:center}
.lead{font-size:14px;line-height:22px;color:var(--text)}
.centered.lead{left:360px;width:480px}

/* header */
.site-header{top:0;left:0;width:1200px;height:120px}
.brand{left:72px;top:30px;display:flex;flex-direction:column;align-items:center;gap:4px}
.brand-mark{width:26px;height:26px;border-radius:50%;background:var(--red)}
.brand-name{font-size:13px;font-weight:700;color:var(--ink);letter-spacing:1px;text-align:center;line-height:14px}
.main-nav{left:500px;top:52px;display:flex;gap:20px;font-size:13px;color:var(--text);white-space:nowrap}
.main-nav .active{color:var(--red)}
.apply-btn{left:985px;top:34px;width:140px;height:54px;background:var(--red);color:var(--white);border-radius:6px;font-size:15px}

/* hero */
.hero{top:120px;left:0;width:1200px;height:660px;background:linear-gradient(100deg,#2f3a45 0%,#556270 45%,#8b949b 70%,#5c6a52 100%)}
.hero-title{left:72px;top:100px;font-size:54px;font-weight:800;line-height:60px;color:var(--white);width:560px}
.hero-text{left:72px;top:292px;width:500px;font-size:14px;line-height:22px;color:var(--white)}
.hero .btn-blue{left:72px;top:415px}

/* about */
.about-title{left:72px;top:985px}
.about-text{left:72px;top:1048px;width:480px;font-size:13px;line-height:20px}
.about .btn-blue{left:72px;top:1195px}
.about-photo{left:595px;top:870px;width:530px;height:460px;border-radius:18px;background:linear-gradient(135deg,#c6a887,#6e7e8c 55%,#2f4560)}

/* services */
.services-title{top:1390px}
.services-lead{top:1462px}
.service-card{top:1565px;width:328px;height:340px;background:var(--white);border-radius:4px;box-shadow:0 4px 18px rgba(0,0,0,.1);text-align:center;padding:38px 30px 0}
.service-card svg{display:block;margin:0 auto 20px}
.service-card h3{font-size:17px;font-weight:600;color:var(--blue-title);margin-bottom:16px}
.service-card p{font-size:13px;line-height:20px;color:var(--text)}
.service-card .more{position:absolute;left:0;right:0;bottom:40px;font-size:14px;color:var(--text)}

/* business */
.business-title{top:1985px}
.business-lead{top:2055px}
.business-photo{top:2150px;width:328px;height:320px;border-radius:4px}
.business-photo .btn-ghost{position:absolute;left:89px;top:138px}

/* personal */
.personal{top:2560px;left:0;width:1200px;height:520px;background:linear-gradient(90deg,#fff 0%,#fff 30%,#e5e7ea 48%,#2b46a8 68%,#1a2f7a 100%)}
.personal-title{left:72px;top:125px}
.personal-text{left:72px;top:185px;width:460px}
.personal .btn-blue{left:72px;top:300px}

/* feature strip */
.strip-card{top:3095px;height:375px;overflow:hidden}
.strip-band{left:0;bottom:0;width:100%;height:62px;background:linear-gradient(90deg,rgba(200,16,46,.92),var(--red-dark));display:flex;align-items:center;justify-content:space-between;padding:0 40px 0 36px;color:var(--white);font-size:15px;font-weight:600}
.strip-band .btn-ghost{width:120px;height:40px;font-size:14px}

/* reasons */
.reasons-title{top:3535px}
.reasons{top:3640px;left:0;width:1200px;height:570px;background:linear-gradient(90deg,#6a7078 0%,#b5b9bd 35%,#eef0f1 52%,#fff 70%)}
.reasons-panel{left:620px;top:70px;width:500px;height:490px;background:var(--red);border-radius:6px;padding:38px 34px}
.faq-open{background:var(--white);color:var(--ink);height:46px;border-radius:4px;display:flex;align-items:center;justify-content:space-between;padding:0 18px;font-size:14px}
.faq-answer{color:var(--white);font-size:13px;line-height:20px;font-weight:600;padding:16px 18px 18px}
.faq-item{border-bottom:1px solid rgba(255,255,255,.6);height:60px;display:flex;align-items:center;justify-content:space-between;padding:0 18px;color:var(--white);font-size:14px;font-weight:600}

/* footer */
.site-footer{top:4330px;left:0;width:1200px;height:480px;background:var(--footer)}
.footer-brand{left:120px;top:95px}
.footer-about{left:120px;top:225px;width:230px;font-size:13px;line-height:20px;color:var(--text)}
.footer-col{top:125px}
.footer-col h4{font-size:18px;font-weight:600;color:var(--blue-title);margin-bottom:20px}
.footer-col li{list-style:none;font-size:13px;line-height:20px;color:var(--text)}
.newsletter-field{margin-top:4px;width:235px;height:36px;border:1px solid #bdbdbd;display:flex;align-items:center;justify-content:space-between;padding:0 10px;font-size:12px;color:var(--muted)}
.copyright{top:4810px;left:0;width:1200px;height:70px;background:#111;color:var(--white);font-size:14px;display:flex;align-items:center;justify-content:center}
</style>
</head>
<body>

<header class="site-header abs">
  <a class="brand abs" href="#">
    <span class="brand-mark"></span>
    <span class="brand-name">RIDGELINE<br>INSURANCE</span>
  </a>
  <nav class="main-nav abs">
    <a class="active" href="#">Home</a>
    <a href="#">About us</a>
    <a href="#">Services</a>
    <a href="#">Business</a>
    <a href="#">Personal</a>
    <a href="#">Contact</a>
  </nav>
  <a class="apply-btn btn abs" href="#">Apply Now</a>
</header>

<section class="hero abs" role="img" aria-label="White semi truck on a highway with a smiling insurance agent in a hard hat and safety vest">
  <h1 class="hero-title abs">WELCOME TO RIDGELINE INSURANCE</h1>
  <p class="hero-text abs">Lorem Ipsum is simply dummy text of the printing and typesetting industry. Lorem Ipsum has been the industry's standard dummy text ever since the 1500s, when an unknown printer took a galley of type and scrambled it to make a type specimen book.</p>
  <a class="btn btn-blue abs" href="#">Learn More</a>
</section>

<section class="about">
  <h2 class="section-title about-title abs"><span class="accent">About</span> us</h2>
  <p class="lead about-text abs">Lorem Ipsum is simply dummy text of the printing and typesetting industry. Lorem Ipsum has been the industry's standard dummy text ever since the 1500s.Lorem Ipsum is simply dummy text of the printing and typesetting industry. Lorem Ipsum has been the industry's standard dummy text ever since the 1500s.</p>
  <a class="btn btn-blue abs" href="#">Read More</a>
  <div class="about-photo abs" role="img" aria-label="Trucker and agent reviewing a clipboard beside a blue truck"></div>
</section>

<section class="services">
  <h2 class="section-title services-title centered abs"><span class="accent">Our</span> Services</h2>
  <p class="lead services-lead centered abs">Lorem Ipsum is simply dummy text of the printing and typesetting industry. Lorem Ipsum has been the industry's standard dummy text ever since the 1500s.</p>

  <article class="service-card abs" style="left:72px">
    <svg width="44" height="44" viewBox="0 0 44 44" fill="none" stroke="#333" stroke-width="1.6"><circle cx="22" cy="9" r="5"/><path d="M13 22c0-5 4-7 9-7s9 2 9 7"/><circle cx="11" cy="27" r="4"/><circle cx="33" cy="27" r="4"/><path d="M3 40c0-4 3-6 8-6s8 2 8 6M25 40c0-4 3-6 8-6s8 2 8 6"/></svg>
    <h3>Trucking Insurance Family</h3>
    <p>Lorem Ipsum is simply dummy text of the printing and typesetting industry. Lorem Ipsum has been the industry's standard dummy text ever since the 1500s.</p>
    <a class="more" href="#">Read More</a>
  </article>
  <article class="service-card abs" style="left:436px">
    <svg width="44" height="44" viewBox="0 0 44 44" fill="none" stroke="#333" stroke-width="1.6"><circle cx="24" cy="10" r="6"/><path d="M24 7v6M4 30h8l8 4h10l8-6M12 30v10h-8"/><path d="M20 34l-2-4h10"/></svg>
    <h3>Trucking Insurance Family</h3>
    <p>Lorem Ipsum is simply dummy text of the printing and typesetting industry. Lorem Ipsum has been the industry's standard dummy text ever since the 1500s.</p>
    <a class="more" href="#">Read More</a>
  </article>
  <article class="service-card abs" style="left:800px">
    <svg width="44" height="44" viewBox="0 0 44 44" fill="none" stroke="#333" stroke-width="1.6"><path d="M22 4l16 8H6z"/><path d="M9 14v18M17 14v18M27 14v18M35 14v18M4 36h36M4 40h36"/></svg>
    <h3>Trucking Insurance Future</h3>
    <p>Lorem Ipsum is simply dummy text of the printing and typesetting industry. Lorem Ipsum has been the industry's standard dummy text ever since the 1500s.</p>
    <a class="more" href="#">Read More</a>
  </article>
</section>

<section class="business">
  <h2 class="section-title business-title centered abs"><span class="accent">Our</span> Business</h2>
  <p class="lead business-lead centered abs">Lorem Ipsum is simply dummy text of the printing and typesetting industry. Lorem Ipsum has been the industry's standard dummy text ever since the 1500s.</p>
  <div class="business-photo abs" style="left:72px;background:linear-gradient(180deg,#a9c4dd,#e7ecef 50%,#7f8589)" role="img" aria-label="Row of white semi trucks parked in a lot"></div>
  <div class="business-photo abs" style="left:436px;background:linear-gradient(180deg,#4b5866,#6f7a64 60%,#3a3f44)" role="img" aria-label="Workers in safety vests at a truck depot">
    <a class="btn btn-ghost" href="#">Read More</a>
  </div>
  <div class="business-photo abs" style="left:800px;background:linear-gradient(160deg,#e9ecee,#c9ced2 50%,#8a9a4a)" role="img" aria-label="Driver in a safety vest climbing into a truck cab"></div>
</section>

<section class="personal abs" role="img" aria-label="Smiling trucker with crossed arms in front of a blue truck">
  <h2 class="section-title personal-title abs"><span class="accent">Personal</span> Work</h2>
  <p class="lead personal-text abs">Lorem Ipsum is simply dummy text of the printing and typesetting industry. Lorem Ipsum has been the industry's standard dummy text ever since the 1500s.</p>
  <a class="btn btn-blue abs" href="#">Read More</a>
</section>

<div class="strip-card abs" style="left:0;width:596px;background:linear-gradient(180deg,#b7cce0,#e5ecf2 40%,#2d4ca0 70%,#6c747c)" role="img" aria-label="Blue semi truck on a wide road">
  <div class="strip-band abs"><span>Lorem Ipsum is simply dummy text</span><a class="btn btn-ghost" href="#">Read More</a></div>
</div>
<div class="strip-card abs" style="left:604px;width:596px;background:linear-gradient(180deg,#8aa7c4,#cfd7dc 45%,#8d9a8b 75%,#5d6660)" role="img" aria-label="Convoy of semi trucks and a tanker on a highway">
  <div class="strip-band abs"><span>Lorem Ipsum is simply dummy text</span><a class="btn btn-ghost" href="#">Read More</a></div>
</div>

<h2 class="section-title reasons-title centered abs"><span class="accent">Top</span> Reasons</h2>
<section class="reasons abs" role="img" aria-label="Trucker in a plaid shirt standing beside a parked trailer">
  <div class="reasons-panel abs">
    <div class="faq-open"><span>Lorem Ipsum is simply dummy text of</span>
      <svg width="14" height="14" viewBox="0 0 14 14" fill="none" stroke="#333" stroke-width="2"><path d="M3 5l4 4 4-4"/></svg></div>
    <p class="faq-answer">Lorem Ipsum is simply dummy text of the printing and typesetting industry. Lorem Ipsum has been the industry's standard dummy text ever since the 1500s.</p>
    <div class="faq-item"><span>Lorem Ipsum is simply dummy text of</span><svg width="14" height="14" viewBox="0 0 14 14" fill="none" stroke="#fff" stroke-width="2"><path d="M3 5l4 4 4-4"/></svg></div>
    <div class="faq-item"><span>Lorem Ipsum is simply dummy text of</span><svg width="14" height="14" viewBox="0 0 14 14" fill="none" stroke="#fff" stroke-width="2"><path d="M3 5l4 4 4-4"/></svg></div>
    <div class="faq-item"><span>Lorem Ipsum is simply dummy text of</span><svg width="14" height="14" viewBox="0 0 14 14" fill="none" stroke="#fff" stroke-width="2"><path d="M3 5l4 4 4-4"/></svg></div>
    <div class="faq-item"><span>Lorem Ipsum is simply dummy text of</span><svg width="14" height="14" viewBox="0 0 14 14" fill="none" stroke="#fff" stroke-width="2"><path d="M3 5l4 4 4-4"/></svg></div>
    <div class="faq-item"><span>Lorem Ipsum is simply dummy text of</span><svg width="14" height="14" viewBox="0 0 14 14" fill="none" stroke="#fff" stroke-width="2"><path d="M3 5l4 4 4-4"/></svg></div>
  </div>
</section>

<footer class="site-footer abs">
  <div class="brand footer-brand abs">
    <span class="brand-mark"></span>
    <span class="brand-name">RIDGELINE<br>INSURANCE</span>
  </div>
  <p class="footer-about abs">Lorem Ipsum is simply dummy text of the printing and typesetting industry. Lorem Ipsum has been the industry's standard dummy text ever since the 1500s.</p>
  <div class="footer-col abs" style="left:450px">
    <h4>About us</h4>
    <ul><li>Home</li><li>About us</li><li>Services</li><li>Blog</li></ul>
  </div>
  <div class="footer-col abs" style="left:640px">
    <h4>Information</h4>
    <ul><li>Privacy Policy</li><li>Terms</li><li>Contact us</li></ul>
  </div>
  <div class="footer-col abs" style="left:885px">
    <h4>Newsletter</h4>
    <div class="newsletter-field"><span>Email</span>
      <svg width="16" height="16" viewBox="0 0 16 16" fill="none" stroke="#555" stroke-width="1.4"><path d="M1 8l14-6-5 13-2-5z"/><path d="M8 10l7-8"/></svg></div>
  </div>
</footer>
<div class="copyright abs">Copyright Reserved @ 2023</div>

</body>
</html>
```